New Website Design for PALVO.org

We are looking for a new website design for PALVO.org. PALVO is a non profit home inspector association based in California. Home Inspectors are people that come out and look at a house before it's purchased to let the buyer know of any defects that may exist.
Our site is based on Joomla so if you'll be able to make a Joomla 3 template as well, please let us know (not required, but a bonus).
We would like to see designs that incorporate royal blue, white and chrome into the site as that's our main business colors.
We would like a place for rotating banners though they don't need to be the same size as the current site.
We would like navigation to be easier to manage with menus only across the top (via drop down menus) where we are going to sort out the items currently on the side. Possibly the front page could have a graphic link to separate portals for Realtors, Home Buyers and Inspectors, but that's just one option.
We would like a good mobile design or something that will scale easily to mobile.
The Find an Inspector feature is important and should stand out. The ZIM PALVOr site
Current home page feels a bit busy. Would like to simplify a bit.

```html
<!DOCTYPE html>
<html lang="en">
<head>
<meta charset="utf-8">
<title>PALVO — Find an Inspector</title>
<link href="https://fonts.googleapis.com/css2?family=Arimo:ital,wght@0,400;0,700;1,700&family=Merriweather:wght@700&display=swap" rel="stylesheet">
<style>
  :root {
    --navy-dark: #1c2140;
    --navy-mid: #2b3356;
    --cyan: #3cc6ee;
    --royal: #1a5cbf;
    --royal-deep: #0b3f93;
    --chrome: #a8acb1;
    --slate: #1f2a33;
    --slate-light: #34434f;
    --white: #ffffff;
    --paper: #f3f4f5;
    --ink: #111111;
    --gold: #f2b705;
    --social: #2f6fb5;
  }
  * { margin: 0; padding: 0; box-sizing: border-box; }
  html, body { width: 1200px; height: 902px; overflow: hidden; background: var(--white); }
  body { position: relative; font-family: "Arimo", Arial, sans-serif; }

  .help-bar {
    position: absolute; left: 0; top: 0; width: 1200px; height: 47px;
    background: linear-gradient(var(--navy-mid), var(--navy-dark));
  }
  .help-icon { position: absolute; left: 74px; top: 6px; }
  .help-line {
    position: absolute; left: 130px; top: 12px;
    font-style: italic; font-weight: 700; font-size: 20px; color: var(--white);
    letter-spacing: 0.3px;
  }
  .help-line .help-label { color: var(--cyan); margin-right: 6px; }
  .social-links { position: absolute; left: 1002px; top: 10px; display: flex; gap: 11px; }
  .social-dot {
    width: 27px; height: 27px; border-radius: 50%;
    background: radial-gradient(circle at 35% 30%, #7fb2e6, var(--social) 55%, #1d4f8c);
    box-shadow: 0 0 0 2px #4a7fbd, 0 1px 2px rgba(0,0,0,0.5);
  }

  .site-header {
    position: absolute; left: 0; top: 47px; width: 1200px; height: 248px;
    background: linear-gradient(#ffffff, var(--paper));
  }
  .brand {
    position: absolute; left: 55px; top: 21px; width: 206px; height: 206px;
    border-radius: 50%; background: var(--navy-dark);
    display: flex; align-items: center; justify-content: center;
    font-weight: 700; font-size: 40px; color: var(--white); letter-spacing: 2px;
  }
  .inspector-search { position: absolute; left: 788px; top: 47px; width: 350px; height: 126px; }
  .inspector-search::before, .inspector-search::after {
    content: ""; position: absolute; left: 0; width: 350px; height: 10px;
    background: radial-gradient(ellipse at center, rgba(0,0,0,0.16), rgba(0,0,0,0) 70%);
  }
  .inspector-search::before { top: 0; }
  .inspector-search::after { bottom: 0; }
  .field-label { position: absolute; top: 28px; font-size: 13px; color: var(--ink); }
  .field-input {
    position: absolute; top: 44px; width: 118px; height: 24px;
    background: var(--white); border: 1px solid #b9bcc0;
  }
  .search-button {
    position: absolute; left: 46px; top: 76px; width: 253px; height: 32px;
    background: linear-gradient(#1d5ea8, #0c3570);
    color: var(--white); font-size: 13px; text-align: center; line-height: 30px;
    border: 1px solid #0a2c5c;
  }

  .main-nav {
    position: absolute; left: 0; top: 295px; width: 1200px; height: 55px;
    background: linear-gradient(var(--royal), var(--royal-deep));
    border-top: 2px solid #0a2f6e;
    display: flex; align-items: center; padding-left: 100px; gap: 23px;
    color: var(--white); font-size: 15px;
  }

  .hero {
    position: absolute; left: 0; top: 350px; width: 1200px; height: 459px;
    background:
      linear-gradient(180deg, rgba(60,80,95,0) 55%, rgba(20,30,40,0.6) 80%, rgba(15,22,30,0.9)),
      linear-gradient(90deg, #2a3944, #1c2731 50%, #2a3944);
  }
  .hero-curve {
    position: absolute; left: -120px; top: 728px; width: 400px; height: 220px;
    border-radius: 50%; background: #eef5fb;
  }
  .slider-frame {
    position: absolute; left: 58px; top: 380px; width: 1062px; height: 448px;
    border: 7px solid var(--chrome); background: var(--chrome);
  }
  .slide-image {
    position: absolute; inset: 0;
    background:
      radial-gradient(ellipse 35% 45% at 58% 48%, rgba(255,255,255,0.75), rgba(255,255,255,0) 70%),
      radial-gradient(ellipse 40% 60% at 12% 30%, rgba(70,62,58,0.55), rgba(70,62,58,0) 70%),
      radial-gradient(ellipse 45% 35% at 80% 95%, rgba(60,54,50,0.5), rgba(60,54,50,0) 70%),
      linear-gradient(120deg, #8a827d, #c9c4c0 45%, #e2dfdc 60%, #a9a29d 85%, #7d7570);
  }
  .slide-caption {
    position: absolute; left: 0; right: 0; bottom: 0; height: 60px;
    background: rgba(40,48,55,0.85);
    color: var(--white); font-family: "Merriweather", Georgia, serif; font-weight: 700;
    font-size: 24px; letter-spacing: 0.6px; text-align: center; line-height: 58px;
  }
  .slider-arrow {
    position: absolute; top: 588px; width: 34px; height: 34px;
    background: var(--gold); box-shadow: 0 3px 0 #a77c00;
    color: var(--ink); font-size: 24px; text-align: center; line-height: 32px;
  }
  .slider-arrow.prev { left: 47px; }
  .slider-arrow.next { left: 1097px; }
</style>
</head>
<body>
  <div class="help-bar">
    <svg class="help-icon" width="44" height="34" viewBox="0 0 44 34" aria-hidden="true">
      <circle cx="14" cy="9" r="6" fill="#8fd3f2"/>
      <circle cx="30" cy="9" r="6" fill="#8fd3f2"/>
      <path d="M3 28c0-8 5-12 11-12s11 4 11 12z" fill="#8fd3f2"/>
      <path d="M19 28c0-8 5-12 11-12s11 4 11 12z" fill="#8fd3f2"/>
      <circle cx="22" cy="24" r="8" fill="#ffffff"/>
      <path d="M18.5 21.5c1 3 3 5 6 6l1.5-1.5" stroke="#2b3356" stroke-width="2" fill="none"/>
    </svg>
    <p class="help-line"><span class="help-label">NEED HELP -</span>(800) 555-0142 OR &nbsp;(916) 555-0187</p>
    <div class="social-links">
      <span class="social-dot"></span>
      <span class="social-dot"></span>
      <span class="social-dot"></span>
    </div>
  </div>

  <header class="site-header">
    <div class="brand">PALVO</div>
    <form class="inspector-search">
      <span class="field-label" style="left:48px">Distance</span>
      <span class="field-label" style="left:183px">From</span>
      <span class="field-input" style="left:44px"></span>
      <span class="field-input" style="left:181px"></span>
      <div class="search-button">SEARCH FOR A INSPECTOR</div>
    </form>
  </header>

  <nav class="main-nav">
    <span>Home</span><span>|</span>
    <span>Find an Inspector</span><span>|</span>
    <span>Home Buyers &amp; Sellers</span><span>|</span>
    <span>Real Estate Agents</span><span>|</span>
    <span>Inspectors</span><span>|</span>
    <span>Ask PALVO</span><span>|</span>
    <span>Conferences</span>
  </nav>

  <section class="hero" role="img" aria-label="Dark city skyline at dusk behind the banner"></section>
  <div class="hero-curve"></div>

  <div class="slider-frame">
    <div class="slide-image" role="img" aria-label="Hands passing a floating house icon among rows of digital house listings"></div>
    <div class="slide-caption">REAL ANSWERS FROM SEASONED INSPECTORS</div>
  </div>
  <div class="slider-arrow prev">&lt;</div>
  <div class="slider-arrow next">&gt;</div>
</body>
</html>
```